Need to drive pregnant women to my 3d4d ultrasound studio where i provide 4d ultrasound with hyperalistic imaging and gender reveals

Industry/Entity Type

Healthcare

Font styles to use
Decorative
Script

Requirements
Must have
• My Company name Latido de Luna 4D. EVERYTHING HAS TO BE IN SPANISH
Nice to have
• SIMPLE AND NOT TOO BUSY
Should not have
• website

```html
<!DOCTYPE html>
<html lang="es">
<head>
<meta charset="utf-8">
<title>Latido de Luna 4D – Banner</title>
<link href="https://fonts.googleapis.com/css2?family=Poppins:wght@400;600;700;800&family=Titan+One&family=Oswald:wght@300;500;600&display=swap" rel="stylesheet">
<style>
  :root{
    --page:#7b7b7b;
    --pink-bg-top:#f8cfe0;
    --pink-bg-bottom:#fdeef4;
    --ink:#1c1c1c;
    --pink:#ee6f9c;
    --pink-band:#e57598;
    --blue:#4396dd;
    --purple:#5b3c8c;
    --logo-purple:#9a6ac0;
    --white:#ffffff;
  }
  *{margin:0;padding:0;box-sizing:border-box}
  html,body{width:1200px;height:1200px;overflow:hidden;background:var(--page)}
  .banner{
    position:absolute;left:76px;top:338px;width:1048px;height:524px;overflow:hidden;
    background:linear-gradient(180deg,var(--pink-bg-top) 0%,#fbdfeb 45%,var(--pink-bg-bottom) 100%);
    font-family:"Poppins",sans-serif;color:var(--ink);
  }
  .headline{position:absolute;left:43px;top:38px;font-weight:700;font-size:50px;line-height:50px;letter-spacing:.3px}
  .headline-accent{position:absolute;left:43px;top:152px;font-family:"Titan One",sans-serif;color:var(--pink);font-size:56px;line-height:58px;letter-spacing:.5px}
  .icon{position:absolute}
  .feature-band{position:absolute;left:47px;top:281px;width:755px;height:72px;border-radius:18px;overflow:hidden;display:flex}
  .feature-4d{width:415px;background:var(--blue);color:var(--white);display:flex;align-items:center;padding-left:22px}
  .feature-4d .big{font-family:"Oswald",sans-serif;font-weight:600;font-size:48px;line-height:1;margin-right:12px}
  .feature-4d .lines{font-weight:700;font-size:18.5px;line-height:23px}
  .feature-4d .light{font-weight:400}
  .feature-gender{flex:1;background:var(--pink-band);color:var(--white);display:flex;align-items:center;padding-left:14px}
  .feature-gender .special{font-family:"Oswald",sans-serif;font-weight:500;font-size:23px;margin-left:10px;letter-spacing:.2px;white-space:nowrap}
  .feature-gender .special span{font-weight:300}
  .feature-gender .divider{width:1.5px;height:44px;background:rgba(255,255,255,.8);margin:0 12px}
  .feature-gender .reveal{font-weight:600;font-size:18px;line-height:22px;white-space:nowrap}
  .brand{position:absolute;left:40px;top:404px;width:136px;display:flex;align-items:center;gap:6px;flex-direction:column;text-align:center}
  .brand-dot{width:34px;height:34px;border-radius:50%;background:var(--logo-purple)}
  .brand-name{font-weight:600;font-size:15px;line-height:18px;color:var(--logo-purple)}
  .tagline{position:absolute;left:193px;top:370px;font-size:18.5px;white-space:nowrap}
  .tagline b{font-weight:700}
  .contact{position:absolute;left:194px;top:420px;display:flex;align-items:center;white-space:nowrap}
  .phone-icon{width:27px;height:27px;border-radius:50%;background:var(--purple);display:flex;align-items:center;justify-content:center;margin-right:13px}
  .phone{font-weight:700;font-size:30px;letter-spacing:.5px}
  .contact .sep{width:1.5px;height:34px;background:#aaa;margin:0 17px}
  .follow{font-size:27px}
  .social-square{width:20px;height:20px;border-radius:4px;background:var(--blue);margin-left:12px}
  .photo-frame{position:absolute;background:var(--white);box-shadow:0 2px 6px rgba(0,0,0,.15);padding:17px}
  .photo-frame .photo{width:100%;height:100%}
  .frame-scan{left:513px;top:38px;width:166px;height:157px}
  .frame-scan .photo{background:radial-gradient(ellipse at 45% 45%,#d98a3a 0%,#a5531c 55%,#3e1607 100%)}
  .frame-newborn{left:652px;top:97px;width:182px;height:176px;transform:rotate(9deg)}
  .frame-newborn .photo{background:radial-gradient(ellipse at 50% 55%,#f1c4ab 0%,#d89a86 60%,#5a2a22 100%)}
  .mother-photo{position:absolute;left:830px;top:34px;width:218px;height:490px;border-radius:110px 110px 0 0;background:linear-gradient(180deg,#5b3427 0%,#e5b7a4 30%,#d9b3b3 45%,#1f1b1d 60%,#141214 100%)}
</style>
</head>
<body>
<main class="banner">
  <h1 class="headline">Ve a Tu Bebé<br>en Asombroso</h1>
  <p class="headline-accent">DETALLE ANTES<br>DE NACER</p>

  <svg class="icon" style="left:461px;top:91px" width="38" height="38" viewBox="0 0 38 38" aria-hidden="true">
    <circle cx="24" cy="14" r="10" fill="none" stroke="var(--pink)" stroke-width="3"/>
    <line x1="17" y1="21" x2="4" y2="34" stroke="var(--pink)" stroke-width="3"/>
    <line x1="5" y1="25" x2="14" y2="34" stroke="var(--pink)" stroke-width="3"/>
  </svg>
  <svg class="icon" style="left:378px;top:219px" width="46" height="46" viewBox="0 0 46 46" aria-hidden="true">
    <circle cx="14" cy="14" r="11" fill="none" stroke="var(--blue)" stroke-width="3.5"/>
    <line x1="22" y1="22" x2="40" y2="40" stroke="var(--blue)" stroke-width="3.5"/>
    <polygon points="44,44 30,41 41,30" fill="var(--blue)"/>
  </svg>
  <svg class="icon" style="left:508px;top:223px" width="30" height="30" viewBox="0 0 30 30" aria-hidden="true">
    <polygon points="15,2 19,11 28,12 21,18 23,28 15,23 7,28 9,18 2,12 11,11" fill="#5bc0ea"/>
  </svg>
  <svg class="icon" style="left:727px;top:48px" width="44" height="40" viewBox="0 0 44 40" aria-hidden="true">
    <path d="M22 38 C6 26 2 18 2 11 C2 5 7 1 12 1 C17 1 20 4 22 8 C24 4 27 1 32 1 C37 1 42 5 42 11 C42 18 38 26 22 38Z" fill="#f7a3cd"/>
  </svg>

  <div class="photo-frame frame-scan"><div class="photo" role="img" aria-label="Imagen de ultrasonido 4D del rostro de un bebé"></div></div>
  <div class="photo-frame frame-newborn"><div class="photo" role="img" aria-label="Foto de un recién nacido dormido"></div></div>

  <div class="mother-photo" role="img" aria-label="Foto de una mujer embarazada sonriendo y sosteniendo su vientre"></div>

  <div class="feature-band">
    <div class="feature-4d">
      <span class="big">4D</span>
      <span class="lines">ULTRASONIDO <span class="light">CON</span><br>IMÁGENES HIPERREALISTAS</span>
    </div>
    <div class="feature-gender">
      <svg width="40" height="50" viewBox="0 0 46 50" aria-hidden="true">
        <circle cx="18" cy="24" r="10" fill="none" stroke="#fff" stroke-width="2.5"/>
        <circle cx="27" cy="24" r="10" fill="none" stroke="#fff" stroke-width="2.5"/>
        <line x1="11" y1="17" x2="3" y2="9" stroke="#fff" stroke-width="2.5"/>
        <polyline points="2,15 3,9 9,8" fill="none" stroke="#fff" stroke-width="2.5"/>
        <line x1="27" y1="34" x2="27" y2="47" stroke="#fff" stroke-width="2.5"/>
        <line x1="21" y1="42" x2="33" y2="42" stroke="#fff" stroke-width="2.5"/>
      </svg>
      <span class="special">EXPERTOS <span>EN</span></span>
      <span class="divider"></span>
      <span class="reveal">REVELACIÓN<br>DE GÉNERO</span>
    </div>
  </div>

  <div class="brand">
    <span class="brand-dot"></span>
    <span class="brand-name">Latido de Luna 4D</span>
  </div>

  <p class="tagline">Tu Viaje a la <b>MATERNIDAD, BELLAMENTE CAPTURADA</b></p>

  <div class="contact">
    <span class="phone-icon">
      <svg width="15" height="15" viewBox="0 0 24 24" aria-hidden="true"><path d="M6.6 10.8a15 15 0 0 0 6.6 6.6l2.2-2.2c.3-.3.7-.4 1-.2 1.1.4 2.300.6 3.6.6.6 0 1 .4 1 1V20c0 .6-.4 1-1 1A17 17 0 0 1 3 4c0-.6.4-1 1-1h3.5c.6 0 1 .4 1 1 0 1.3.2 2.5.6 3.6.1.3 0 .7-.2 1z" fill="#fff"/></svg>
    </span>
    <span class="phone">+1 555-014-2387</span>
    <span class="sep"></span>
    <span class="follow">síguenos en</span>
    <span class="social-square"></span>
  </div>
</main>
</body>
</html>
```